Webdesign Tischlerei Wallbusch
Zielgruppe
es handelt sich um eine Tischlerei / Meisterbetrieb
Zielgruppe: private und gwerbliche Kunden
Aufgabenstellung
- die Vielfältigkeit der Produkte aus eigener Herstellung durch Meisterhand soll vermittelt werden
- FixWerk Systemspezialist
- Produktschulungen Kork
- KEINE Kopie der alten Seite
- aufgelockert und modern
- gern mit Elementen in leichter Holzoptik und weichen Rundungen
- Farben modern und in Telen an das Logo angepasst
Vorstellung des Kunden zur Navigationsstruktur:
Navigationsstruktur Website
1. wo arbeiten wir... (in der Werkstatt findet mittlerweile der geringere Anteil der Arbeit statt)
• Bild Werkstatt von außen/Schild
• Mitarbeiter an der Säge
• und/oder Mitarbeiter an der Hobelmaschine
• Gespräch/Planung/Skizzen
• evtl. (gepacktes) Fahrzeug(denn das ist ein wichtiges Arbeitsmittel)
2. was macht uns aus...
• vernünftiges Verhältnis zu den Mitarbeitern, ermöglicht eine kontinuierliche, fachgerechte und qualitativ hochwertige Arbeit an den Projekten
• überwiegend handwerkliche Fertigung
• Verwendung von Materialien und Hölzern- auch aus der Region
• Flexibilität im Umgang mit Arbeitszeit, Material und Leistungen
3. welche Möglichkeiten haben wir....
• „Liste“ mit den Möglichkeiten die wir so haben(z.B. Herstellung und Reparaturen von individuellen Treppen, Möbeln, Türen, Lieferung und Reparatur von Fenstern, verlegen und reparieren von Fußböden wie Hobeldielen, Parkett, Designböden, Carport, Zäune, Tore
• Galerie Projekte mit Beschreibung
• vorher-nachher Bilder mit Beschreibung
4. was sollte Sie interessieren...
• Tipps &Tricks rund ums Holz/Produkte(Fenster Pflegehinweise)
• Termine und Veranstaltungen auch nicht betrieblich
• Empfehlungen (Produkte, Materialien, Pflegemittel -was wir benutzen und gefällt oder ist das dann Werbung?)
5. womit könnten wir ihnen helfen...
• Interaktives Anfrageformular
• Möglichkeit Skizzen hochzuladen, Wünsche zu beschreiben
6. wie erreichen Sie uns...<..

```html
<!DOCTYPE html>
<html lang="de">
<head>
<meta charset="utf-8">
<title>Tischlerei Wallbusch</title>
<link rel="stylesheet" href="https://fonts.googleapis.com/css2?family=Manrope:wght@500;600;700;800&family=Inter:wght@400;500;600&display=swap">
<style>
:root{
  --blue:#0b5391;
  --ink:#1d1b19;
  --text:#3c3a37;
  --muted:#5a5550;
  --accent:#7a6a45;
  --tan:#efe3c9;
  --footer:#f4e6c4;
  --page:#fbf7f5;
  --band:#f4f1ef;
  --line:#e6e0da;
}
*{box-sizing:border-box;margin:0;padding:0}
html,body{width:1200px;height:2988px;overflow:hidden}
body{background:var(--page);font-family:"Inter",sans-serif;color:var(--text);position:relative}
.abs{position:absolute}
h1,h2,h3{font-family:"Manrope",sans-serif;color:var(--ink)}

.site-header{left:0;top:0;width:1200px;height:110px;background:#fff;box-shadow:0 2px 10px rgba(0,0,0,.05);border-radius:0 0 10px 10px}
.brand{left:40px;top:34px;display:flex;align-items:center;gap:10px;font-family:"Manrope",sans-serif;font-weight:800;font-size:22px;color:var(--blue)}
.brand-dot{width:14px;height:14px;border-radius:50%;background:var(--blue)}
.nav{left:480px;top:46px;display:flex;gap:24px;font-family:"Manrope",sans-serif;font-weight:600;font-size:14px;color:#333}
.nav .active{color:var(--blue);border-bottom:2px solid var(--blue);padding-bottom:5px;margin-top:-3px}
.tools{right:32px;top:44px;display:flex;gap:33px}

.hero{left:14px;top:118px;width:1172px;height:767px;border-radius:14px;overflow:hidden;
  background:linear-gradient(90deg,#fbf6f1 0%,#f5ebe0 38%,#d9c2a7 70%,#a98d75 100%)}
.hero-fade{inset:0;background:linear-gradient(180deg,rgba(255,255,255,0) 70%,rgba(251,247,245,.9) 100%)}
.badge{left:46px;top:200px;height:34px;padding:0 16px;border-radius:17px;background:rgba(220,212,200,.6);display:flex;align-items:center;gap:8px;font-family:"Manrope",sans-serif;font-weight:600;font-size:14px;color:#5a5048}
.hero h1{left:46px;top:262px;font-size:62px;font-weight:800;line-height:69px;letter-spacing:-1px}
.hero h1 .hl{color:var(--blue)}
.hero p{left:46px;top:502px;width:520px;font-size:17.5px;line-height:27.5px;color:#3a3530}
.btn{top:630px;height:57px;border-radius:8px;display:flex;align-items:center;justify-content:center;gap:10px;font-family:"Manrope",sans-serif;font-weight:700;font-size:14.5px}
.btn-primary{left:46px;width:201px;background:var(--blue);color:#fff}
.btn-ghost{left:263px;width:189px;border:2px solid #777;color:#222}

.work h2{left:20px;top:1170px;font-size:40px;font-weight:700}
.rule{height:3px;width:62px;background:var(--accent)}
.work .lead{left:18px;top:1282px;width:560px;font-size:17.5px;line-height:27.5px}
.work .note{left:18px;top:1420px;width:560px;font-size:15.5px;line-height:24.5px}
.photo{border-radius:12px;box-shadow:0 6px 14px rgba(0,0,0,.12)}

.values{left:0;top:1732px;width:1200px;height:573px;background:var(--band)}
.values h2{left:0;width:1200px;top:1808px;text-align:center;font-size:40px;font-weight:700}
.values .sub{left:0;width:1200px;top:1895px;text-align:center;font-size:17.5px}
.card{top:1948px;width:268px;height:332px;background:#fbf8f6;border-radius:12px;box-shadow:0 2px 8px rgba(0,0,0,.04);padding:30px 30px}
.card .ico{width:52px;height:60px;border-radius:8px;background:var(--tan);display:flex;align-items:center;justify-content:center}
.card h3{margin-top:28px;font-size:24px;font-weight:500;line-height:29px}
.card p{margin-top:22px;font-size:15.5px;line-height:24.5px;color:var(--muted)}

.options h2{left:22px;top:2380px;font-size:40px;font-weight:700;line-height:47px}
.options .lead{left:22px;top:2528px;width:360px;font-size:17.5px;line-height:27.5px}
.opt{top:2382px;width:240px}
.opt .circ{width:46px;height:46px;border-radius:50%;background:#e4ebf1;display:flex;align-items:center;justify-content:center}
.opt h3{margin-top:28px;font-size:20px;font-weight:500;line-height:29px}
.opt ul{margin-top:22px;list-style:none;font-size:15.5px}
.opt li{height:37px;display:flex;align-items:center;gap:9px}
.opt li::before{content:"";width:5px;height:5px;border-radius:50%;background:#555}

.site-footer{left:0;top:2858px;width:1200px;height:130px;background:var(--footer);border-radius:26px 26px 0 0}
.site-footer .brand{left:36px;top:56px;font-size:19px}
.foot-links{right:32px;top:64px;display:flex;gap:31px;font-size:14px;color:#6d88a8}
</style>
</head>
<body>

<header class="site-header abs">
  <div class="brand abs"><span class="brand-dot"></span>Tischlerei Wallbusch</div>
  <nav class="nav abs"><span>About</span><span>Services</span><span>Projects</span><span class="active">Workshop</span></nav>
  <div class="tools abs">
    <svg width="22" height="22" viewBox="0 0 24 24" fill="none" stroke="#0b5391" stroke-width="1.8" stroke-linecap="round" stroke-linejoin="round"><path d="M22 16.9v3a2 2 0 0 1-2.2 2 19.8 19.8 0 0 1-8.6-3.1 19.5 19.5 0 0 1-6-6A19.8 19.8 0 0 1 2.1 4.2 2 2 0 0 1 4.1 2h3a2 2 0 0 1 2 1.7c.1 1 .4 1.9.7 2.8a2 2 0 0 1-.5 2.1L8 9.9a16 16 0 0 0 6 6l1.3-1.3a2 2 0 0 1 2.1-.4c.9.3 1.8.6 2.8.7a2 2 0 0 1 1.7 2z"/></svg>
    <svg width="22" height="22" viewBox="0 0 24 24" fill="none" stroke="#0b5391" stroke-width="1.8" stroke-linejoin="round"><rect x="2" y="4" width="20" height="16" rx="2"/><path d="M2 6l10 7 10-7"/></svg>
    <svg width="22" height="22" viewBox="0 0 24 24" fill="none" stroke="#0b5391" stroke-width="1.8" stroke-linejoin="round"><path d="M3 7h4l2-3h6l2 3h4v13H3z"/><circle cx="12" cy="13" r="4"/></svg>
  </div>
</header>

<section class="hero abs" role="img" aria-label="Tischler bearbeitet ein Holzbrett, Sägestaub im Gegenlicht">
  <div class="hero-fade abs"></div>
  <div class="badge abs">
    <svg width="14" height="14" viewBox="0 0 24 24" fill="none" stroke="#5a5048" stroke-width="2.2" stroke-linecap="round"><path d="M4 20l8-8M14 4l6 6M20 20l-7-7M4 4l4 4"/></svg>
    Tradition trifft Innovation
  </div>
  <h1 class="abs">Meisterhafte<br><span class="hl">Handwerkskunst</span><br>aus Holz</h1>
  <p class="abs">Wir schaffen maßgeschneiderte Lösungen, die Generationen überdauern. Von der ersten Skizze bis zur finalen Montage vereinen wir präzises Handwerk mit modernster Technik.</p>
  <a class="btn btn-primary abs">Anfrage senden
    <svg width="16" height="16" viewBox="0 0 24 24" fill="none" stroke="#fff" stroke-width="2.4" stroke-linecap="round" stroke-linejoin="round"><path d="M5 12h14M13 6l6 6-6 6"/></svg></a>
  <a class="btn btn-ghost abs">Projekte ansehen</a>
</section>

<section class="work">
  <h2 class="abs">Wo wir arbeiten</h2>
  <div class="rule abs" style="left:20px;top:1240px"></div>
  <p class="lead abs">Unsere moderne Werkstatt ist das Herzstück unseres Schaffens, aber unsere Arbeit endet nicht an der Werkstatttür. Wir sind ein mobiles Team, das die Qualität der Werkbank direkt zu Ihnen nach Hause bringt.</p>
  <p class="note abs">Ausgestattet mit professionellen Montagefahrzeugen garantieren wir eine saubere, präzise und termingerechte Umsetzung Ihrer Projekte vor Ort. Wir planen flexibel und agieren lösungsorientiert in Ihrem Umfeld.</p>
  <div class="photo abs" style="left:625px;top:994px;width:265px;height:263px;background:linear-gradient(180deg,#5d8fd0 0%,#a9c6e4 35%,#c98a4c 60%,#3a3a3c 100%)" role="img" aria-label="Werkstattgebäude mit Holzfassade unter blauem Himmel"></div>
  <div class="photo abs" style="left:625px;top:1273px;width:266px;height:332px;background:linear-gradient(160deg,#b4652a 0%,#e8e4de 40%,#dcd6ce 70%,#9c5424 100%)" role="img" aria-label="Möbelskizzen auf Papier mit Bleistiften auf einem Holztisch"></div>
  <div class="photo abs" style="left:905px;top:1040px;width:263px;height:331px;background:linear-gradient(160deg,#6e4a2c 0%,#b68a5e 40%,#e0cdb0 70%,#c9b089 100%)" role="img" aria-label="Hand misst ein Holzbrett mit gelbem Maßband"></div>
  <div class="photo abs" style="left:905px;top:1387px;width:264px;height:266px;background:linear-gradient(180deg,#9bb7d3 0%,#6f8f4f 30%,#e8e9ea 55%,#3f4246 80%,#8b8e90 100%)" role="img" aria-label="Gepackter Transporter mit geöffneten Hecktüren"></div>
</section>

<section class="values abs"></section>
<h2 class="abs" style="left:0;width:1200px;top:1808px;text-align:center;font-size:40px;font-weight:700">Was uns ausmacht</h2>
<div class="rule abs" style="left:565px;top:1868px"></div>
<p class="abs" style="left:0;width:1200px;top:1895px;text-align:center;font-size:17.5px">Werte, die in jedem unserer Werkstücke spürbar sind.</p>

<article class="card abs" style="left:26px">
  <div class="ico"><svg width="26" height="26" viewBox="0 0 24 24" fill="none" stroke="#7a6a45" stroke-width="1.8" stroke-linecap="round" stroke-linejoin="round"><path d="M12 2l2.4 1.8 3 .1.9 2.8 2.4 1.8-.9 2.8.9 2.8-2.4 1.8-.9 2.8-3 .1L12 22l-2.4-1.8-3-.1-.9-2.8-2.4-1.8.9-2.8-.9-2.8 2.4-1.8.9-2.8 3-.1z"/><path d="M8.5 12l2.5 2.5 4.5-5"/></svg></div>
  <h3>Qualität &amp;<br>Präzision</h3>
  <p>Wir arbeiten auf den Millimeter genau, um makellose Ergebnisse zu liefern, die höchsten Ansprüchen genügen.</p>
</article>
<article class="card abs" style="left:319px">
  <div class="ico"><svg width="26" height="26" viewBox="0 0 24 24" fill="none" stroke="#7a6a45" stroke-width="2" stroke-linecap="round"><path d="M4 20l9-9M14 4l6 6M16 6l-3 3M20 20l-6-6M4 4l3 3"/></svg></div>
  <h3>Handwerkliche<br>Fertigung</h3>
  <p>Jedes Stück ist ein Unikat, das mit traditionellen Techniken und viel Liebe zum Detail gefertigt wird.</p>
</article>
<article class="card abs" style="left:612px">
  <div class="ico"><svg width="26" height="26" viewBox="0 0 24 24" fill="none" stroke="#7a6a45" stroke-width="1.8" stroke-linejoin="round"><path d="M8 3l-5 9h3l-4 7h12l-4-7h3z"/><path d="M16 5l-3 5h2l-2 4h8l-3-4h2z"/></svg></div>
  <h3>Regionale<br>Materialien</h3>
  <p>Wir beziehen unsere Hölzer vorzugsweise aus heimischen Wäldern und legen Wert auf nachhaltige Forstwirtschaft.</p>
</article>
<article class="card abs" style="left:905px">
  <div class="ico"><svg width="26" height="26" viewBox="0 0 24 24" fill="none" stroke="#7a6a45" stroke-width="2" stroke-linecap="round" stroke-linejoin="round"><path d="M9 7H5v4M5 7a7 7 0 0 1 4 11M15 17h4v-4M19 17a7 7 0 0 1-4-11"/></svg></div>
  <h3>Flexibilität</h3>
  <p>Wir passen uns Ihren Wünschen und zeitlichen Vorgaben an und finden für jede räumliche Herausforderung eine Lösung.</p>
</article>

<section class="options">
  <h2 class="abs">Unsere<br>Möglichkeiten</h2>
  <div class="rule abs" style="left:22px;top:2497px"></div>
  <p class="lead abs">Ein breites Spektrum an handwerklichen Dienstleistungen, ausgeführt mit meisterlicher Expertise.</p>
  <div class="opt abs" style="left:422px">
    <div class="circ"><svg width="16" height="16" viewBox="0 0 24 24" fill="#0b5391"><path d="M6 3l8 8-3 3-8-8zM13 13l3-3 6 9-2 2z"/></svg></div>
    <h3>Handwerkliche<br>Herstellung</h3>
    <ul><li>Treppen</li><li>Türen &amp; Tore</li><li>Möbel</li><li>Carports</li><li>Gartenmöbel</li></ul>
  </div>
  <div class="opt abs" style="left:685px">
    <div class="circ"><svg width="16" height="16" viewBox="0 0 24 24" fill="#0b5391"><path d="M21 6a5 5 0 0 1-7 5l-8 9-3-3 9-8a5 5 0 0 1 5-7l-3 3 1 3 3 1z"/></svg></div>
    <h3>Reparatur &amp;<br>Instandsetzung</h3>
    <ul><li>Fenster</li><li>Türen</li><li>Möbel</li><li>Parkettböden</li></ul>
  </div>
  <div class="opt abs" style="left:948px">
    <div class="circ"><svg width="18" height="18" viewBox="0 0 24 24" fill="#0b5391"><path d="M9 4h6v3h6v13H3V7h6zm2 1v2h2V5z"/></svg></div>
    <h3>Montage</h3>
    <ul><li>Fenster</li><li>Türen</li><li>Treppen</li><li>Möbel</li></ul>
  </div>
</section>

<footer class="site-footer abs">
  <div class="brand abs"><span class="brand-dot"></span>Tischlerei Wallbusch</div>
  <nav class="foot-links abs"><span>Imprint</span><span>Privacy Policy</span><span>Terms of Service</span><span>Contact</span></nav>
</footer>

</body>
</html>
```